Business Card Design

We need a business card for a new furniture company in Utah. We are introducing a fresh new concept in Utah and would like a card to reflect to buyers that they can buy quality furniture and get it NOW. I am open to just about any color scheme, but I would like something that pops.

Industry/Entity Type

Business

Contact Information for Business Card

Sofa Haven, Glen Marsh
41 S. Pine Hollow Lane
Cedar Brook Utah 84217

```html
<!DOCTYPE html>
<html lang="en">
<head>
<meta charset="utf-8">
<title>Sofa Haven – Business Card</title>
<link rel="stylesheet" href="https://fonts.googleapis.com/css2?family=Cinzel:wght@500&family=Tinos:wght@400&display=swap">
<style>
  :root {
    --page-bg: #f4f2ef;
    --card-dark: #241812;
    --card-mid: #3b2a20;
    --band: #2a1a12;
    --gold: #d9a93c;
    --gold-light: #f3d27a;
    --gold-deep: #a8741e;
    --text-light: #ffffff;
  }
  * { margin: 0; padding: 0; box-sizing: border-box; }
  html, body {
    width: 1200px;
    height: 900px;
    overflow: hidden;
    background: var(--page-bg);
  }
  .canvas {
    position: relative;
    width: 1200px;
    height: 900px;
  }
  .business-card {
    position: absolute;
    left: 110px;
    top: 160px;
    width: 980px;
    height: 580px;
    border-radius: 42px;
    overflow: hidden;
    box-shadow: 0 18px 40px rgba(0,0,0,0.25);
  }
  .damask-field {
    position: absolute;
    inset: 0;
    background: radial-gradient(ellipse at 55% 45%, var(--card-mid) 0%, var(--card-dark) 85%);
  }
  .holder-name {
    position: absolute;
    top: 58px;
    right: 48px;
    font-family: "Tinos", "Times New Roman", serif;
    font-size: 26px;
    color: var(--gold);
    letter-spacing: 0.5px;
  }
  .ornament {
    position: absolute;
    left: 330px;
    width: 420px;
    height: 130px;
    background: radial-gradient(ellipse at 50% 50%, var(--gold-light) 0%, var(--gold) 40%, rgba(168,116,30,0.6) 65%, rgba(168,116,30,0) 72%);
  }
  .ornament--top { top: 80px; }
  .ornament--bottom { top: 320px; }
  .title-band {
    position: absolute;
    left: 0;
    right: 0;
    top: 212px;
    height: 108px;
    background: var(--band);
    border-top: 3px solid var(--gold);
    border-bottom: 3px solid var(--gold);
    display: flex;
    align-items: center;
    justify-content: center;
    padding-left: 100px;
  }
  .title-band::before,
  .title-band::after {
    content: "";
    position: absolute;
    left: 0; right: 0;
    height: 1px;
    background: var(--gold-deep);
  }
  .title-band::before { top: 7px; }
  .title-band::after { bottom: 7px; }
  .wordmark {
    font-family: "Cinzel", Georgia, serif;
    font-weight: 500;
    font-size: 68px;
    color: var(--gold);
    letter-spacing: 3px;
  }
  .contact-list {
    position: absolute;
    left: 58px;
    top: 398px;
    list-style: none;
    font-family: "Tinos", "Times New Roman", serif;
    font-size: 25px;
    line-height: 31px;
    color: var(--text-light);
  }
  .contact-list li {
    display: flex;
    align-items: center;
    gap: 12px;
  }
  .contact-list .icon {
    width: 24px;
    height: 24px;
    flex: none;
    fill: var(--gold);
  }
  .contact-list .indent { padding-left: 36px; }
</style>
</head>
<body>
<div class="canvas">
  <div class="business-card">
    <div class="damask-field" role="img" aria-label="Dark brown damask wallpaper pattern"></div>

    <div class="holder-name">Glen Marsh</div>

    <div class="ornament ornament--top" role="img" aria-label="Gold baroque flourish ornament above the title"></div>
    <div class="ornament ornament--bottom" role="img" aria-label="Gold baroque flourish ornament below the title"></div>

    <div class="title-band">
      <span class="wordmark">Sofa Haven</span>
    </div>

    <ul class="contact-list">
      <li>
        <svg class="icon" viewBox="0 0 24 24" aria-hidden="true"><path d="M6.6 10.8c1.4 2.8 3.8 5.1 6.6 6.6l2.2-2.2c.3-.3.7-.4 1-.2 1.1.4 2.3.6 3.6.6.6 0 1 .4 1 1V20c0 .6-.4 1-1 1C10.6 21 3 13.4 3 4c0-.6.4-1 1-1h3.5c.6 0 1 .4 1 1 0 1.3.2 2.5.6 3.6.1.3 0 .7-.2 1l-2.3 2.2z"/></svg>
        <span>1555 217 904</span>
      </li>
      <li>
        <svg class="icon" viewBox="0 0 24 24" aria-hidden="true"><path d="M12 2a10 10 0 100 20 10 10 0 000-20zm6.9 6h-3a15 15 0 00-1.3-4A8 8 0 0118.9 8zM12 4c.8 1.2 1.5 2.5 1.9 4h-3.8c.4-1.5 1.1-2.8 1.9-4zM4.3 14a8 8 0 010-4h3.4a16 16 0 000 4H4.3zm.8 2h3a15 15 0 001.3 4A8 8 0 015.1 16zm3-8h-3a8 8 0 014.3-4A15 15 0 008.1 8zM12 20c-.8-1.2-1.5-2.5-1.9-4h3.8c-.4 1.5-1.1 2.8-1.9 4zm2.3-6H9.7a14 14 0 010-4h4.6a14 14 0 010 4zm.3 6a15 15 0 001.3-4h3a8 8 0 01-4.3 4zm1.7-6a16 16 0 000-4h3.4a8 8 0 010 4h-3.4z"/></svg>
        <span>www.sofahaven.com</span>
      </li>
      <li>
        <svg class="icon" viewBox="0 0 24 24" aria-hidden="true"><path d="M3 6h18v12H3z" opacity=".35"/><path d="M3 6l9 7 9-7v2l-9 7-9-7z"/></svg>
        <span>info@sofahaven.com</span>
      </li>
      <li>
        <svg class="icon" viewBox="0 0 24 24" aria-hidden="true"><path d="M12 3l10 9h-3v8h-5v-6h-4v6H5v-8H2z"/></svg>
        <span>41 S. Pine Hollow Lane</span>
      </li>
      <li class="indent"><span>Cedar Brook Utah 84217</span></li>
    </ul>
  </div>
</div>
</body>
</html>
```